Need corporate powerpoint template design for our sales proposals

Need corporate power point design template for our sales proposals. This powerpoint will be targeted at our customers when we are putting design proposals and pricing quotes together for them

Target Market(s)

Our customers

Industry/Entity Type

Sales

Requirements
Must have
• Brookvane name and logo somewhere
• Would like to have a cover slide and then non-cover slide as well as an ending slide for powerpoint templates
• Must have our corporate address and contact info somewhere, they are: Brookvane, Inc PO Box 47193 Fernhill, Oregon 97321. Office # 510-384-7159, email is info@brookvane-example.com
• I also attached an example business card to give you a sense of our design, also our website is www.brookvane-example.com
• Would like to match existing color scheme

```html
<!DOCTYPE html>
<html lang="en">
<head>
<meta charset="utf-8">
<title>Brookvane Sales Proposal Template</title>
<link href="https://fonts.googleapis.com/css2?family=Oswald:wght@300;400&family=Open+Sans:wght@400;600;700&display=swap" rel="stylesheet">
<style>
:root{
  --bg:#c9c9c9;
  --green:#7a9a3a;
  --green-mid:#8fb04a;
  --green-light:#9dbf55;
  --green-pale:#eef3e2;
  --green-bright:#1aae4e;
  --mint:#d9f0e2;
  --teal:#1f5f6b;
  --orange:#e07a1f;
  --ink:#555;
  --white:#fff;
}
*{box-sizing:border-box;margin:0;padding:0}
html,body{width:808px;height:1200px;overflow:hidden;background:var(--bg)}
body{position:relative;font-family:"Open Sans",Arial,sans-serif;color:var(--ink)}
.slide{position:absolute;width:288px;height:216px;background:var(--white);overflow:hidden;box-shadow:0 2px 4px rgba(0,0,0,.25)}
.abs{position:absolute}
.photo{position:absolute}
.head{font-family:"Oswald",Arial,sans-serif;font-weight:400;text-transform:uppercase;letter-spacing:-.2px}

/* cover */
.cover .logo{left:106px;width:104px;text-align:center;top:100px;font-family:"Open Sans",sans-serif;font-weight:400;font-size:15px;color:var(--green)}
.cover .contact{left:113px;width:90px;top:172px;font-size:3.4px;line-height:4.4px;color:#333;text-align:center;font-weight:600}

/* feature three */
.features .title{top:26px;width:100%;text-align:center;color:#fff;font-size:13px;line-height:20px;font-weight:400}
.features .box{left:29px;top:84px;width:230px;height:132px;background:#fff}
.feat{position:absolute;top:10px;width:60px;text-align:center}
.feat .lab{color:var(--green-bright);font-size:4.4px;font-weight:700;margin:4px 0 3px}
.feat p{font-size:3.6px;line-height:5.3px;color:#333}

/* list */
.list .title{top:24px;width:100%;text-align:center;color:var(--green-mid);font-size:16px}
.list .sub{top:46px;width:100%;text-align:center;color:var(--teal);font-size:5px}
.row{position:absolute;left:21px;width:136px;height:25px;display:flex}
.row .num{width:22px;background:var(--green);color:#fff;font-size:7px;font-weight:600;display:flex;align-items:center;justify-content:center}
.row .txt{flex:1;padding:3px 4px;background:var(--green-pale)}
.row.alt .txt{background:#e4ebf6}
.row .txt b{display:block;font-size:4px;color:#333;font-weight:600;margin-bottom:2px}
.row .txt span{display:block;font-size:3px;line-height:3.8px;color:#999}

/* team */
.team .title{top:20px;width:100%;text-align:center;color:var(--green-mid);font-size:16px}
.team .band{left:0;top:110px;width:288px;height:106px;background:var(--green)}
.member{position:absolute;top:76px;width:70px;text-align:center}
.member .face{width:64px;height:64px;margin:0 auto;border-radius:50%;border:2px solid var(--green-light);background:radial-gradient(circle at 50% 45%,#c9a58a,#5e5249)}
.member .name{color:#fff;font-family:"Oswald",sans-serif;font-size:7.5px;margin-top:8px}
.member .role{color:#e6eed6;font-size:3.8px}

/* quality */
.quality{background:linear-gradient(135deg,#6f9a45,#8fae5c 60%,#6d8f43)}
.quality .title{top:22px;width:100%;text-align:center;color:#fff;font-size:10.5px;font-weight:300}
.quality .box{left:32px;top:51px;width:227px;height:145px;background:#fff}
.quality .qh{left:188px;top:68px;color:var(--green);font-size:10px}
.quality ul{position:absolute;left:170px;top:96px;width:80px;list-style:disc;font-size:3.8px;line-height:5.4px;color:#444}

/* icon list */
.iconlist{background:linear-gradient(90deg,#8fb04a 0%,#97b55c 55%,#9aaa8e 100%)}
.iconlist .lead{left:14px;top:40px;width:90px;text-align:center;color:#fff;font-size:6.8px;line-height:9.6px}
.iconlist .box{left:113px;top:14px;width:141px;height:187px;background:#fff}
.item{position:absolute;left:0;width:141px;text-align:center}
.item p{font-size:3.3px;line-height:4.6px;color:#666;padding:0 12px;margin-top:3px}

/* profile */
.profile .band{left:0;top:167px;width:288px;height:49px;background:var(--green-light)}
.profile .title{left:138px;top:25px;color:var(--green);font-size:13px}
.profile .sub{left:138px;top:45px;color:var(--orange);font-size:5px;font-weight:600}
.profile ul{position:absolute;left:146px;top:62px;font-size:4px;line-height:5.6px;list-style:disc;color:#555}
.profile .lbl{left:138px;top:96px;color:var(--orange);font-size:4px;font-weight:700}
.profile .para{left:138px;top:106px;width:136px;font-size:3.8px;line-height:5.4px;color:#555}
.profile .band-text{left:118px;top:180px;width:160px;text-align:center;color:#fff;font-size:9px}

/* services */
.services .title{top:20px;width:100%;text-align:center;color:var(--green-mid);font-size:13px}
.svc{position:absolute;top:63px;width:120px;height:125px;border-bottom:2px solid var(--green-light)}
.svc .hd{height:18px;color:#fff;font-size:5px;font-weight:600;display:flex;align-items:center;justify-content:center}
.svc p{padding:20px 8px 0;text-align:center;font-size:5.3px;line-height:8.6px;color:#333}
</style>
</head>
<body>

<!-- Cover -->
<section class="slide cover" style="left:116px;top:127px">
  <div class="photo" role="img" aria-label="Photo of business people shaking hands" style="left:0;top:0;width:106px;height:216px;background:linear-gradient(160deg,#6c7d8c,#a9b4bd 50%,#4d5a66)"></div>
  <div class="photo" role="img" aria-label="Photo of smiling colleagues applauding" style="left:210px;top:0;width:78px;height:216px;background:linear-gradient(200deg,#cfd8de,#6e7e8c 55%,#3e4a55)"></div>
  <div class="abs logo">Brookvane</div>
  <div class="abs contact">Brookvane, Inc<br>PO Box 47193 Fernhill,<br>Oregon 97321<br><br>510-384-7159<br>info@brookvane-example.com</div>
</section>

<!-- Three features -->
<section class="slide features" style="left:435px;top:127px;background:linear-gradient(180deg,#7fa046,#8fb04a 60%,#90a27a)">
  <div class="abs head title">Lorem ipsum dolor sit amet<br>consectetur adipiscing elit.</div>
  <div class="abs box">
    <div class="feat" style="left:14px">
      <svg width="16" height="16" viewBox="0 0 16 16"><rect x="1" y="1" width="14" height="11" rx="2" fill="var(--green-light)"/><circle cx="6" cy="6" r="2" fill="#fff"/><circle cx="10" cy="6" r="2" fill="#fff"/><path d="M6 12l2 3 2-3z" fill="var(--green-light)"/></svg>
      <div class="lab">LOREM IPSUM</div>
      <p>Lorem ipsum dolor sit amet consectetur adipiscing elit. Cras bibendum mattis leo, ac efficitur ipsum lobortis non. Praesent vitae pulvinar metus. Phasellus accumsan elementum condimentum. Nullam rutrum, tellus tincidunt scelerisque elementum</p>
    </div>
    <div class="feat" style="left:85px">
      <svg width="16" height="16" viewBox="0 0 16 16" fill="var(--green-light)"><path d="M8 1l7 4H1z"/><rect x="2" y="6" width="2" height="7"/><rect x="5.5" y="6" width="2" height="7"/><rect x="9" y="6" width="2" height="7"/><rect x="12" y="6" width="2" height="7"/><rect x="1" y="13" width="14" height="2"/></svg>
      <div class="lab">LOREM IPSUM</div>
      <p>Lorem ipsum dolor sit amet consectetur adipiscing elit. Cras bibendum mattis leo, ac efficitur ipsum lobortis non. Praesent vitae pulvinar metus. Phasellus accumsan elementum condimentum. Nullam rutrum, tellus tincidunt scelerisque elementum</p>
    </div>
    <div class="feat" style="left:156px">
      <svg width="16" height="16" viewBox="0 0 16 16" fill="var(--green-light)"><path d="M1 3h5l2 2h7v9H1z"/></svg>
      <div class="lab">LOREM IPSUM</div>
      <p>Lorem ipsum dolor sit amet consectetur adipiscing elit. Cras bibendum mattis leo, ac efficitur ipsum lobortis non. Praesent vitae pulvinar metus. Phasellus accumsan elementum condimentum. Nullam</p>
    </div>
  </div>
</section>

<!-- Numbered list -->
<section class="slide list" style="left:116px;top:370px">
  <div class="abs head title">Lorem ipsum dolor sit amet</div>
  <div class="abs head sub">Consectetur adipiscing elit. Cras</div>
  <div class="row" style="top:70px"><div class="num">01</div><div class="txt"><b>Lorem ipsum dolor sit amet</b><span>Lorem ipsum dolor sit amet consectetur adipiscing elit.</span><span>Cras bibendum mattis leo. Lorem ipsum dolor sit amet</span></div></div>
  <div class="row alt" style="top:99px"><div class="num">02</div><div class="txt"><b>Lorem ipsum dolor sit amet</b><span>Lorem ipsum dolor sit amet consectetur adipiscing elit.</span><span>Cras bibendum mattis leo. Lorem ipsum dolor sit amet</span></div></div>
  <div class="row" style="top:128px"><div class="num">03</div><div class="txt"><b>Lorem ipsum dolor sit amet</b><span>Lorem ipsum dolor sit amet consectetur adipiscing elit.</span><span>Cras bibendum mattis leo. Lorem ipsum dolor sit amet</span></div></div>
  <div class="row alt" style="top:157px"><div class="num">04</div><div class="txt"><b>Lorem ipsum dolor sit amet</b><span>Lorem ipsum dolor sit amet consectetur adipiscing elit.</span><span>Cras bibendum mattis leo. Lorem ipsum dolor sit amet</span></div></div>
  <div class="photo" role="img" aria-label="Photo of a hand using a tablet over financial charts" style="left:165px;top:70px;width:109px;height:112px;background:linear-gradient(150deg,#dfe9f1,#9fb8cc 50%,#e9eef2)"></div>
</section>

<!-- Team -->
<section class="slide team" style="left:435px;top:370px">
  <div class="abs head title">Out team members</div>
  <div class="abs band"></div>
  <div class="member" style="left:31px"><div class="face" role="img" aria-label="Portrait photo of a team member"></div><div class="name">LOREM IPSUM</div><div class="role">LOREM IPSUM</div></div>
  <div class="member" style="left:109px"><div class="face" role="img" aria-label="Portrait photo of a team member"></div><div class="name">LOREM IPSUM</div><div class="role">LOREM IPSUM</div></div>
  <div class="member" style="left:186px"><div class="face" role="img" aria-label="Portrait photo of a team member"></div><div class="name">LOREM IPSUM</div><div class="role">LOREM IPSUM</div></div>
</section>

<!-- Quality -->
<section class="slide quality" style="left:116px;top:614px">
  <div class="abs head title">Lorem ipsum dolor sit amet consectetur</div>
  <div class="abs box"></div>
  <div class="photo" role="img" aria-label="Photo of a smiling team around a laptop" style="left:32px;top:51px;width:136px;height:124px;background:linear-gradient(160deg,#e8eef2,#a7b6c2 55%,#3f4f62)"></div>
  <div class="abs head qh">Quality</div>
  <ul>
    <li>Lorem ipsum dolor sit amet consectetur adipiscing elit. Cras</li>
    <li>Lorem ipsum dolor sit amet consectetur adipiscing elit. Cras</li>
    <li>Lorem ipsum dolor sit amet consectetur adipiscing elit. Cras</li>
    <li>Lorem ipsum dolor sit amet consectetur adipiscing elit. Cras</li>
    <li>Lorem ipsum dolor sit amet consectetur adipiscing elit. Cras</li>
  </ul>
</section>

<!-- Icon list -->
<section class="slide iconlist" style="left:435px;top:614px">
  <div class="abs lead"><b>Lorem ipsum dolor sit amet consectetur adipiscing elit. Cras bibendum mattis leo, ac efficitur ipsum lobortis non. Praesent vitae pulvinar</b> Lorem ipsum dolor sit amet consectetur adipiscing elit. Cras bibendum mattis leo, ac efficitur ipsum lobortis non. Praesent vitae pulvinar</div>
  <div class="abs box">
    <div class="item" style="top:16px">
      <svg width="20" height="16" viewBox="0 0 20 16" fill="var(--green)"><rect x="7" y="1" width="6" height="3" fill="none" stroke="var(--green)" stroke-width="1.5"/><rect x="1" y="4" width="18" height="11" rx="1.5"/><rect x="1" y="8" width="18" height="1" fill="#fff"/></svg>
      <p>Lorem ipsum dolor sit amet consectetur adipiscing elit. Cras bibendum mattis leo, ac efficitur ipsum lobortis non. Praesent vitae pulvinar metus. Phasellus accumsan elementum condimentum. Nullam rutrum, tellus</p>
    </div>
    <div class="item" style="top:77px">
      <svg width="20" height="16" viewBox="0 0 20 16"><rect x="1" y="1" width="18" height="14" rx="1.5" fill="var(--green)"/><g fill="#fff"><rect x="4" y="5" width="2" height="1.5"/><rect x="8" y="5" width="8" height="1.5"/><rect x="4" y="8" width="2" height="1.5"/><rect x="8" y="8" width="8" height="1.5"/><rect x="4" y="11" width="2" height="1.5"/><rect x="8" y="11" width="8" height="1.5"/></g></svg>
      <p>Lorem ipsum dolor sit amet consectetur adipiscing elit. Cras bibendum mattis leo, ac efficitur ipsum lobortis non. Praesent vitae pulvinar metus. Phasellus accumsan elementum condimentum. Nullam rutrum, tellus</p>
    </div>
    <div class="item" style="top:136px">
      <svg width="22" height="18" viewBox="0 0 22 18" fill="var(--green)"><circle cx="8" cy="10" r="6"/><circle cx="8" cy="10" r="2.2" fill="#fff"/><circle cx="17" cy="5" r="3.5"/><circle cx="17" cy="5" r="1.3" fill="#fff"/></svg>
      <p>Lorem ipsum dolor sit amet consectetur adipiscing elit. Cras bibendum mattis leo, ac efficitur ipsum lobortis non. Praesent vitae pulvinar metus. Phasellus accumsan elementum condimentum. Nullam rutrum, tellus</p>
    </div>
  </div>
</section>

<!-- Profile -->
<section class="slide profile" style="left:116px;top:857px">
  <div class="abs band"></div>
  <div class="photo" role="img" aria-label="Photo of a smiling business team" style="left:18px;top:31px;width:104px;height:157px;background:linear-gradient(160deg,#f0f2f4,#a6afb8 45%,#2f3b4c)"></div>
  <div class="abs head title">Lorem ipsum dolor sit</div>
  <div class="abs sub">LOREM IPSUM DOLOR</div>
  <ul>
    <li>Lorem ipsum dolor sit amet</li>
    <li>consectetur adipiscing elit</li>
    <li>Cras bibendum mattis leo, ac</li>
    <li>efficitur ipsum lobortis non</li>
  </ul>
  <div class="abs lbl">Lorem ipsum dolor:</div>
  <div class="abs para">Lorem ipsum dolor sit amet consectetur adipiscing elit. Cras bibendum mattis leo, ac efficitur ipsum lobortis non. Praesent vitae pulvinar metus. Phasellus accumsan elementum condimentum. Nullam rutrum, tellus tincidunt scelerisque placerat, justo lectus luctus odio, varius auctor urna lacus sed nisl. Suspendisse at placerat sem. Duis tincidunt augue vel eros hendrerit tempus.</div>
  <div class="abs head band-text">Lorem ipsum dolor sit</div>
</section>

<!-- Services -->
<section class="slide services" style="left:435px;top:857px">
  <div class="abs head title">Our services</div>
  <div class="svc" style="left:21px;background:var(--green-pale)">
    <div class="hd" style="background:var(--green)">LOREM IPSUM</div>
    <p>Lorem ipsum dolor sit amet consectetur adipiscing elit. Cras bibendum mattis leo, ac efficitur ipsum lobortis non. Praesent vitae pulvinar metus. Phasellus accumsan elementum condimentum. Nullam rutrum, tellus tincidunt scelerisque elementum</p>
  </div>
  <div class="svc" style="left:151px;background:var(--mint)">
    <div class="hd" style="background:var(--green-bright)">LOREM IPSUM</div>
    <p>Lorem ipsum dolor sit amet consectetur adipiscing elit. Cras bibendum mattis leo, ac efficitur ipsum lobortis non. Praesent vitae pulvinar metus. Phasellus accumsan elementum condimentum. Nullam rutrum, tellus tincidunt scelerisque elementum</p>
  </div>
</section>

</body>
</html>
```